Art for parenting podcast with straight/direct talk...no fluff here! "Plain Word for Families"

I need an image that will not look fluffy or soft. A no-nonsense look. This is not a 'I love parenting' podcast. It is for frustrated parents who don't know what to do. The name is 'Plain Word for Families'. The design should, therefore, NOT have hearts and flowers but, instead, look clean and direct. My logo has shades of blue so that would be nice. I have done this work for over 30 years and am well-degreed so would like the design to look stable/established. I have attached my company's logo.

Target Market(s)

Frustrated parents of children - age birth to 20

Industry/Entity Type

Coaching/Counseling for parents

Font styles to use
Serif
Sans Serif

Colors
0054AA
0677BA
7BADD7
CADEEF
E8F1F8

Requirements
Must have
• A look that is clean/bold/direct and professional. Serious.
Nice to have
• If it looks good, my name with my degrees behind my name. MS, MEd. Another thought would be to have a background image of a frustrated parent. Not sure if that would be good or look too busy.
Should not have
• Flowers, fluff, soft appearance, pinks, light colors

```html
<!DOCTYPE html>
<html lang="en">
<head>
<meta charset="utf-8">
<title>Plain Word for Families Podcast</title>
<link href="https://fonts.googleapis.com/css2?family=Libre+Baskerville:wght@400;700&display=swap" rel="stylesheet">
<style>
  :root {
    --page: #ffffff;
    --navy-top: #1c4896;
    --navy-mid: #23519d;
    --navy-low: #3b66aa;
    --band: #1a78b0;
    --band-dark: #1f4594;
    --shadow: #12306e;
    --white: #ffffff;
  }
  * { margin: 0; padding: 0; box-sizing: border-box; }
  html, body {
    width: 1200px; height: 1200px; overflow: hidden;
    background: var(--page);
    font-family: "Libre Baskerville", "Times New Roman", serif;
  }
  .cover {
    position: absolute; left: 200px; top: 200px;
    width: 800px; height: 800px; overflow: hidden;
    background: linear-gradient(180deg, var(--navy-top) 0%, var(--navy-top) 45%, var(--navy-mid) 70%, var(--navy-low) 100%);
  }
  .cover__photo {
    position: absolute; left: 0; right: 0; top: 380px; bottom: 0;
    background: linear-gradient(180deg, rgba(59,102,170,0) 0%, rgba(80,120,185,0.55) 45%, rgba(95,135,195,0.7) 100%);
  }
  .brand {
    position: absolute; right: 22px; top: 70px;
    display: flex; align-items: center; gap: 8px;
    color: var(--white); font-weight: 700; font-size: 19px; letter-spacing: 0.5px;
  }
  .brand__dot { width: 22px; height: 22px; border-radius: 50%; background: var(--white); }
  .title { position: absolute; left: 0; top: 0; width: 100%; height: 100%; }
  .title__line {
    position: absolute; color: var(--white); line-height: 1; white-space: nowrap;
    transform: rotate(-6deg); transform-origin: left bottom;
    text-shadow: 4px 5px 0 var(--shadow);
  }
  .title__small { left: 70px; top: 95px; font-size: 150px; font-weight: 400; letter-spacing: -3px; }
  .title__big { left: 125px; top: 215px; font-size: 232px; font-weight: 700; letter-spacing: -8px; }
  .title__caps { left: 100px; top: 455px; font-size: 72px; font-weight: 400; letter-spacing: -1px; }
  .ribbon {
    position: absolute; left: 458px; top: 500px; width: 420px; height: 52px;
    background: var(--band);
    transform: rotate(-6deg); transform-origin: left bottom;
    color: var(--white); font-weight: 700; font-size: 28px; letter-spacing: 15px;
    display: flex; align-items: center; padding-left: 26px;
  }
  .host {
    position: absolute; left: 0; right: 0; top: 728px; height: 48px;
    background: var(--band); display: flex; align-items: center;
  }
  .host__label {
    margin-left: 135px; width: 222px; height: 100%;
    background: var(--band-dark); color: var(--white);
    font-weight: 700; font-size: 24px; letter-spacing: -0.5px;
    display: flex; align-items: center; justify-content: center;
  }
  .host__name { margin-left: 12px; color: var(--white); font-size: 23px; letter-spacing: -0.5px; }
</style>
</head>
<body>
  <main class="cover">
    <div class="cover__photo" role="img" aria-label="Blurred photo of a frustrated parent sitting on a sofa holding her head while children rush past"></div>

    <div class="brand"><span class="brand__dot"></span>BRIGHTPATH</div>

    <h1 class="title">
      <span class="title__line title__small">Plain</span>
      <span class="title__line title__big">Word</span>
      <span class="title__line title__caps">FOR FAMILIES</span>
    </h1>

    <div class="ribbon">PODCAST</div>

    <div class="host">
      <span class="host__label">HOSTED BY</span>
      <span class="host__name">MS, MEd. Dana Hollister</span>
    </div>
  </main>
</body>
</html>
```